Redesign of Smart Watch Gift Voucher-SEE ATTACHED CURRENT DESIGN

I need to redesign my existing design using all same content and elements.

MY ENVISION: I invision more of a professional advertisement type of flyer/voucher. Imagine how Corvel.com would create a professionally looking flyer promoting the lumo or veno.

you can get many ideas about professional design by looking at some of corvels flyer designs :
https://www.findora-example.net/search?q=lumo+advertisment&mode=img&ref=a83kd02mzq7

stock photos are attached, you do not have to use them all, you can use some or none i am open to your designs using your own images if you want...just make sure the smartwatch looks black

DO NOT LEAVE ANY CONTENT OR ELEMENTS OUT ON MOCK UP PLEASE

SEE ATTACHED CURRENT DESIGN

I need to redesign my existing design using all same content and elements. DO NOT LEAVE ANY CONTENT OR ELEMENTS OUT ON MOCK UP PLEASE

Target Market(s)

B2B-you can get many ideas about professional design by looking at some of corvels flyer designs :

Industry/Entity Type

Marketing

Requirements
Must have
• I need to redesign my existing design using all same content and elements. DO NOT LEAVE ANY CONTENT OR ELEMENTS OUT ON MOCK UP PLEASE

Nice to have

Should not have

```html
<!DOCTYPE html>
<html lang="en">
<head>
<meta charset="utf-8">
<title>Smart Fitness Watch Reward Certificate</title>
<link rel="stylesheet" href="https://fonts.googleapis.com/css2?family=Montserrat:ital,wght@0,400;0,500;0,600;0,700;0,800;1,500;1,700&family=Damion&display=swap">
<style>
  :root {
    --green: #7dc142;
    --green-deep: #46a302;
    --grey-dark: #58595b;
    --grey-mid: #77787b;
    --charcoal: #2e3038;
    --blue: #1b6cb5;
    --text: #2b2b2b;
    --text-soft: #555;
    --white: #fff;
    --terms: #d8d8d8;
  }
  html, body { margin: 0; padding: 0; overflow: hidden; }
  body { background: #fff; }
  .voucher {
    position: relative; width: 927px; height: 1200px; overflow: hidden;
    background: var(--white); font-family: "Montserrat", sans-serif; color: var(--text);
  }
  .backdrop { position: absolute; inset: 0; }
  .abs { position: absolute; margin: 0; }

  .cert-id { left: 804px; top: 26px; color: var(--white); font-weight: 800; line-height: 1.15; }
  .cert-id .label { font-size: 13px; letter-spacing: .3px; }
  .cert-id .number { font-size: 17.5px; }

  .expiry { right: 364px; top: 78px; text-align: right; font-weight: 800; line-height: 1.1; }
  .expiry .label { font-size: 25px; letter-spacing: 8px; color: #3a3a3a; margin-right: -8px; }
  .expiry .date { font-size: 27px; color: var(--blue); }

  .headline { left: 545px; width: 382px; top: 120px; text-align: center; color: var(--white); }
  .headline .script { font-family: "Damion", cursive; font-size: 100px; line-height: 1; margin: 0 0 0 40px; }
  .headline .title { font-size: 28px; font-weight: 800; line-height: 1; margin: 14px 0 0 0; }
  .headline .rule { width: 295px; height: 1px; background: rgba(255,255,255,.6); margin: 11px auto 12px; }
  .headline .tagline { font-size: 17px; font-weight: 500; line-height: 22px; margin: 0; }

  .testimonial { left: 575px; top: 590px; width: 320px; color: var(--white); }
  .testimonial h2 { font-size: 21px; font-weight: 800; margin: 0 0 18px; }
  .testimonial blockquote { margin: 0; font-style: italic; font-weight: 500; font-size: 15.5px; line-height: 19px; }
  .testimonial cite { display: block; margin-top: 22px; font-style: italic; font-weight: 700; font-size: 16px; }

  .intro { left: 36px; top: 626px; width: 430px; font-size: 11px; line-height: 13.2px; text-align: justify; }
  .how-title { left: 35px; top: 708px; font-size: 21px; font-weight: 800; color: var(--green); }
  .how-body { left: 36px; top: 747px; width: 400px; font-size: 11.2px; line-height: 15.3px; text-align: justify; }

  .features-title { left: 34px; top: 876px; font-size: 29px; font-weight: 800; color: var(--blue); }
  .feature-list { left: 44px; top: 930px; list-style: none; padding: 0; width: 600px;
    display: grid; grid-template-columns: 219px 205px 180px; grid-auto-flow: column; grid-template-rows: repeat(4, 23.5px); }
  .feature-list li { display: flex; align-items: center; gap: 12px; font-size: 11.5px; font-weight: 500; color: var(--text-soft); }
  .feature-list svg { width: 15px; height: 15px; flex: none; }

  .watch { left: 638px; top: 772px; width: 258px; height: 408px; }

  .redeem { left: 126px; top: 1100px; color: var(--white); }
  .redeem .lead { font-size: 14.5px; font-weight: 700; margin: 0; }
  .redeem .url { font-size: 24px; font-weight: 800; margin: 2px 0 0; letter-spacing: .2px; }
  .redeem .terms { font-size: 13px; font-weight: 500; color: var(--terms); margin: 8px 0 0; }
  .gift-icon { left: 36px; top: 1086px; width: 68px; height: 66px; }
</style>
</head>
<body>
<main class="voucher">
  <svg class="backdrop" width="927" height="1200" viewBox="0 0 927 1200" aria-hidden="true">
    <defs>
      <linearGradient id="photoTone" x1="0" y1="0" x2="1" y2="1">
        <stop offset="0" stop-color="#1f6fd1"/>
        <stop offset=".45" stop-color="#2a3550"/>
        <stop offset="1" stop-color="#c9a58f"/>
      </linearGradient>
    </defs>
    <polygon points="755,0 927,0 927,640 870,900 442,895 604,417" fill="var(--grey-dark)"/>
    <polygon points="604,417 927,640 927,700 590,460" fill="var(--charcoal)"/>
    <polygon points="500,394 604,417 540,600" fill="var(--green-deep)"/>
    <polygon points="631,19 927,137 927,640 604,417 497,393" fill="var(--green)"/>
    <polygon points="0,1033 927,1095 927,1200 0,1200" fill="var(--grey-dark)"/>
    <polygon points="45,1053 927,1112 927,1200 45,1200" fill="var(--grey-mid)"/>
  </svg>

  <svg class="abs" style="left:0;top:0" width="560" height="645" viewBox="0 0 560 645" role="img" aria-label="Photo of a runner in a blue shirt checking his phone and black fitness watch">
    <path d="M0,0 L250,0 C360,90 470,160 550,240 L540,640 C330,560 140,400 0,262 Z" fill="url(#photoTone)"/>
  </svg>

  <div class="abs cert-id"><div class="label">CERTIFICATE ID</div><div class="number">91772-89218</div></div>
  <div class="abs expiry"><div class="label">EXPIRES</div><div class="date">10/03/2020</div></div>

  <header class="abs headline">
    <p class="script">Enjoy</p>
    <h1 class="title">YOUR BRANDED NEW<br>SMARTWATCH</h1>
    <div class="rule"></div>
    <p class="tagline">Take Control of your life with your new<br>smart fitness watch</p>
  </header>

  <section class="abs testimonial">
    <h2>WHAT OTHERS SAY</h2>
    <blockquote>"Are you sure this is not a Nexora Orbit Smartwatch in DISGUISE???? I love mine."</blockquote>
    <cite>Dale M. Atlantic City, NJ</cite>
  </section>

  <p class="abs intro">Congratulations, you have been rewarded with a Brand New Smart Fitness Watch shipped right to your door. Just pay shipping and handling. Your new Smart Fitness Watch has these features: sport mode, pedometer, distance, calorie, heart rate, blood pressure, stopwatch, sleep moni- toring, phone locator, reminders, remote camera, an alarm clock and much more!</p>

  <h2 class="abs how-title">HOW CAN WE DO THIS?</h2>
  <p class="abs how-body">We have a couple retail partners that we team up with to "crowd purchase" huge shipping containers that hold 10's of thousands of electronic products at 80-90% off retail. We simply pass our savings on to you as we do not profit from our electronic products. You are basically able to "piggy back" on our partnerships and buying power to get an attractive electronic premium for a fraction of the retail cost.</p>

  <h2 class="abs features-title">FEATURES</h2>
  <svg width="0" height="0" style="position:absolute"><symbol id="tick" viewBox="0 0 16 16"><circle cx="8" cy="8" r="6.5" fill="none" stroke="#3aa935" stroke-width="1.4"/><path d="M4.8 8.2 L7.3 10.6 L13.5 3.2" fill="none" stroke="#3aa935" stroke-width="1.8" stroke-linecap="round"/></symbol></svg>
  <ul class="abs feature-list">
    <li><svg><use href="#tick"/></svg>Pedomoter</li>
    <li><svg><use href="#tick"/></svg>Calorie Counter</li>
    <li><svg><use href="#tick"/></svg>Blood Pressure Monitor</li>
    <li><svg><use href="#tick"/></svg>Sleep Monitoring</li>
    <li><svg><use href="#tick"/></svg>Reminders Feature</li>
    <li><svg><use href="#tick"/></svg>Alarm Clock</li>
    <li><svg><use href="#tick"/></svg>Distance Tracker</li>
    <li><svg><use href="#tick"/></svg>Heart Rate Monitor</li>
    <li><svg><use href="#tick"/></svg>Stopwatch</li>
    <li><svg><use href="#tick"/></svg>Phone Locator</li>
    <li><svg><use href="#tick"/></svg>Remote Camera</li>
    <li><svg><use href="#tick"/></svg>Waterproof</li>
  </ul>

  <svg class="abs watch" viewBox="0 0 258 408" role="img" aria-label="Black smartwatch showing a step counter">
    <defs>
      <linearGradient id="watchTone" x1="0" y1="0" x2="0" y2="1">
        <stop offset="0" stop-color="#3a3b3e"/>
        <stop offset=".5" stop-color="#1a1b1d"/>
        <stop offset="1" stop-color="#333437"/>
      </linearGradient>
    </defs>
    <rect x="0" y="0" width="258" height="408" rx="40" fill="url(#watchTone)"/>
  </svg>

  <svg class="abs gift-icon" viewBox="0 0 68 66" aria-hidden="true" fill="none" stroke="#fff" stroke-width="2" stroke-linejoin="round">
    <rect x="22" y="6" width="40" height="36"/>
    <path d="M34 18 h16 l5 6 -13 12 -13 -12 z M29 24 h26"/>
    <rect x="2" y="50" width="9" height="14"/>
    <path d="M11 52 h16 l10 4 h14 l12 -8 c3 -1 4 2 2 4 l-14 10 h-40"/>
  </svg>

  <div class="abs redeem">
    <p class="lead">View All the Details of This Special Offer and Redeem Online at</p>
    <p class="url">WWW.PERKVAULTOFFERS.COM</p>
    <p class="terms">*Terms and Conditions apply see website for details</p>
  </div>
</main>
</body>
</html>
```